Book cover design for 'Lantern Winter' novel

Title of book 'Lantern Winter'
Subtitle 'a Ness Orford novel'
Author 'T K Halvorsen'
Book genre 'novel - adventure'
Format ' eBook, paperback, audio, thumbnail'
Type 'Self-publishing through PVL'
Trim size 6 x 9
Back cover 'Seeking redemption on the Via de la Plata.
Ness Orford’s life changed forever in a moment of madness. Haunted by his crime, Ness feels a calling to seek redemption on the Camino de Santiago.
The daily toil of walking the Via de la Plata from Seville causes Ness to search his soul.
On The Way Ness encounters other pilgrims with their own personal reasons to answer the call of the camino.
Join Ness for the many highs and lows of camino life as he moves step by step closer to his goal.
Can the Camino give Ness peace of mind and stop his nightmares?'
Overall vision 'The front cover at the top should be the title:
Camino
Calling
This will fill about 20 per cent of the front cover. It must be centre justified. The title should use the same type face as the official Camino de Santiago road sign (see first download). The type should be in bright blue. The background should be in bright yellow.
Under the title should be an image of a path stretching to the horizon with the shadow of a pilgrim (see second download).
Superimposed on the image should be the words 'a Ness Orford novel' maybe using a type face similar to the street signage used in Spain (see third download).
At the bottom of the front cover should be the author's name 'Tom Halvorsen' in the same style as the blue and yellow title - BUT MUCH SMALLER.
On the SPINE of the book should be 'Lantern Winter' and 'Tom Halvorsen' in the blue text on yellow background.
On the back cover there should be a photograph (see fourth download) with the text UPDATE ON THE TEXT 'Seeking redemption on the Via de la Plata.
In a moment of madness Ness Orford’s life changed forever. Haunted by his atrocious act, he feels a calling to seek redemption on the Camino de Santiago.
The daily slog of walking the Via de la Plata from Seville causes Ness to search deep within his soul.
On The Way Ness encounters other pilgrims with their own personal reasons to answer the call of the Camino.
Can the Camino give Ness peace of mind and stop his nightmares?' with a three centimetre space at the bottom for bar code/ISBN and the author headshot photograph attached.

Target Market(s)

Readers who have walked the Camino de Santiago in Spain or who are interested

Requirements
Nice to have
• I would like my headshot (attached) included on the back cover

```html
<!DOCTYPE html>
<html lang="en">
<head>
<meta charset="utf-8">
<title>Lantern Winter – Book Cover</title>
<link rel="stylesheet" href="https://fonts.googleapis.com/css2?family=Poppins:wght@700&family=Dancing+Script:wght@500&display=swap">
<style>
  :root {
    --page: #ffffff;
    --night: #000000;
    --forest-deep: #0d1a0c;
    --forest: #2c4a1f;
    --glow: #e6c93f;
    --glow-soft: #b9a52f;
    --title-blue: #1e9ac8;
    --script-ink: #1a1a10;
  }
  * { margin: 0; padding: 0; box-sizing: border-box; }
  html, body {
    width: 1200px;
    height: 1200px;
    overflow: hidden;
    background: var(--page);
  }
  .canvas {
    position: relative;
    width: 1200px;
    height: 1200px;
    background: var(--page);
  }
  .cover {
    position: absolute;
    left: 200px;
    top: 0;
    width: 800px;
    height: 1200px;
    overflow: hidden;
    background: var(--night);
    box-shadow: 0 0 18px rgba(0,0,0,0.25);
  }
  .cover-scene {
    position: absolute;
    inset: 0;
    background:
      radial-gradient(ellipse 230px 420px at 400px 640px, var(--glow) 0%, var(--glow-soft) 35%, rgba(44,74,31,0.9) 70%, rgba(13,26,12,0) 100%),
      radial-gradient(ellipse 520px 560px at 400px 680px, var(--forest) 0%, var(--forest-deep) 60%, rgba(0,0,0,0) 100%),
      linear-gradient(to bottom, var(--night) 0%, var(--night) 22%, var(--forest-deep) 55%, #050a05 100%);
  }
  .title {
    position: absolute;
    left: 0;
    top: 232px;
    width: 800px;
    text-align: center;
    font-family: "Poppins", sans-serif;
    font-weight: 700;
    font-size: 146px;
    line-height: 194px;
    letter-spacing: -1px;
    color: var(--title-blue);
  }
  .series {
    position: absolute;
    left: 0;
    top: 606px;
    width: 800px;
    text-align: center;
    font-family: "Dancing Script", cursive;
    font-weight: 500;
    font-size: 31px;
    line-height: 48px;
    color: var(--script-ink);
  }
  .author {
    position: absolute;
    left: 0;
    top: 1088px;
    width: 800px;
    text-align: center;
    font-family: "Poppins", sans-serif;
    font-weight: 700;
    font-size: 36px;
    line-height: 50px;
    color: var(--title-blue);
  }
</style>
</head>
<body>
<main class="canvas">
  <section class="cover">
    <div class="cover-scene" role="img" aria-label="Misty forest at dusk with tall dark trees, a yellow glow between them and a hooded pilgrim walking away along the path"></div>
    <h1 class="title">Lantern<br>Winter</h1>
    <p class="series">a Ness Orford<br>novel</p>
    <p class="author">Tom Halvorsen</p>
  </section>
</main>
</body>
</html>
```